Tarvil GmbH business card

We Tarvil GmbH based in Switzerland are looking for a business card design. The Fresh Jung, appealing to customers of all kinds. We already have a logo to upload but still a business card. Details: Tarvil GmbH Address: Lindenweg 14b in 9412 Rudolfen. Tel: 41 76 392 00 47, web: Tarvil.ch, E-mail: info@Tarvil.ch Facebook: Tarvil GmbH. I am the Managing Director: Lukas Verholt. On reverse: Title: Transporter and bus rental Gross: Without deposit Super prices
Contact Information for Business Card
Siehe Projektbeschreibung
Requirements
Should not have
- Other pictures

```html
<!DOCTYPE html>
<html lang="de">
<head>
<meta charset="utf-8">
<title>Tarvil GmbH – Visitenkarte</title>
<link rel="stylesheet" href="https://fonts.googleapis.com/css2?family=Poppins:wght@300;400;500;600;700&display=swap">
<style>
  :root {
    --stage: #000000;
    --paper: #ffffff;
    --navy: #283178;
    --steel: #4f6a9a;
    --steel-light: #7f97b8;
    --mist: #d7dce8;
    --ink-light: #ffffff;
  }
  * { box-sizing: border-box; margin: 0; padding: 0; }
  html, body {
    width: 1200px; height: 900px; overflow: hidden;
    background: var(--stage);
    font-family: "Poppins", sans-serif;
  }
  .stage { position: relative; width: 1200px; height: 900px; }
  .card { position: absolute; overflow: hidden; background: var(--paper); }
  .card svg.card-shapes { position: absolute; inset: 0; }

  /* Front */
  .card-front { left: 377px; top: 128px; width: 412px; height: 271px; }
  .front-brand {
    position: absolute; left: 22px; top: 172px;
    display: flex; align-items: center; gap: 8px;
  }
  .brand-square { width: 40px; height: 40px; background: var(--navy); }
  .brand-text { display: flex; flex-direction: column; }
  .brand-name {
    font-weight: 600; font-size: 24px; line-height: 1; color: var(--navy);
    letter-spacing: 0.5px;
  }
  .brand-tagline {
    font-weight: 400; font-size: 10.5px; color: var(--steel); margin-top: 3px;
  }
  .brand-claims {
    font-weight: 400; font-size: 8px; color: var(--steel);
    margin-top: 2px; padding-left: 38px;
  }
  .front-mark {
    position: absolute; left: 258px; top: 100px; width: 140px;
    text-align: center;
    font-weight: 600; font-size: 34px; color: var(--mist);
  }

  /* Back */
  .card-back { left: 377px; top: 461px; width: 411px; height: 270px; background: var(--steel); }
  .back-mark {
    position: absolute; left: 18px; top: 105px; width: 150px; text-align: center;
    font-weight: 600; font-size: 34px; color: var(--navy);
  }
  .holder { position: absolute; left: 251px; top: 90px; }
  .holder-name { font-size: 14px; font-weight: 600; color: var(--ink-light); line-height: 1.1; }
  .holder-name .surname { color: var(--navy); }
  .holder-role {
    font-size: 8.5px; font-weight: 300; color: var(--mist);
    border-bottom: 1px solid var(--steel-light);
    width: 160px; padding-bottom: 1px; margin-top: 1px;
  }
  .contacts {
    position: absolute; left: 214px; top: 161px; list-style: none;
    font-size: 10px; font-weight: 400; color: var(--ink-light); line-height: 13.2px;
  }
  .contacts li { display: flex; align-items: flex-start; }
  .contacts .icon { width: 16px; height: 13px; flex: none; display: flex; align-items: center; }
  .contacts .icon svg { width: 6px; height: 6px; fill: var(--ink-light); }
</style>
</head>
<body>
<main class="stage">

  <section class="card card-front" aria-label="Vorderseite">
    <svg class="card-shapes" width="412" height="271" viewBox="0 0 412 271">
      <defs>
        <linearGradient id="front-band" x1="0" y1="0" x2="0" y2="1">
          <stop offset="0" stop-color="#7f97b8"/>
          <stop offset="1" stop-color="#283178"/>
        </linearGradient>
      </defs>
      <polygon points="242,142 255,142 279,271 271,271" fill="#4f6a9a"/>
      <polygon points="216,55 326,0 412,0 412,271 279,271 242,142" fill="url(#front-band)"/>
    </svg>
    <div class="front-mark">Tarvil</div>
    <div class="front-brand">
      <span class="brand-square"></span>
      <div class="brand-text">
        <span class="brand-name">TARVIL GMBH</span>
        <span class="brand-tagline">Transporter und Bus Vermietung</span>
        <span class="brand-claims">Ohne Kaution &nbsp;|&nbsp; Super Preise</span>
      </div>
    </div>
  </section>

  <section class="card card-back" aria-label="Rückseite">
    <svg class="card-shapes" width="411" height="270" viewBox="0 0 411 270">
      <polygon points="0,0 83,0 208,60 148,270 0,270" fill="#ffffff"/>
      <polygon points="171,150 180,118 148,270 126,270" fill="#283178"/>
    </svg>
    <div class="back-mark">Tarvil</div>
    <div class="holder">
      <p class="holder-name">Lukas <span class="surname">Verholt</span></p>
      <p class="holder-role">Geschäftsführer</p>
    </div>
    <ul class="contacts">
      <li><span class="icon"><svg viewBox="0 0 10 10"><path d="M2 0l2 2-1 1.5c.6 1.4 1.6 2.4 3 3L7.5 5.5l2 2L8 10C3.5 9.5.5 6.5 0 2z"/></svg></span>+41 76 392 00 47</li>
      <li><span class="icon"><svg viewBox="0 0 10 10"><path d="M0 2h10v6H0z M0 2l5 3.5L10 2" /></svg></span>info@Tarvil.ch</li>
      <li><span class="icon"><svg viewBox="0 0 10 10"><path d="M5 0l5 5H8.5v5h-2.5V7H4v3H1.5V5H0z"/></svg></span>Tarvil.ch</li>
      <li><span class="icon"><svg viewBox="0 0 10 10"><rect width="10" height="10"/></svg></span>Tarvil GmbH.</li>
      <li><span class="icon"><svg viewBox="0 0 10 10"><path d="M5 0a3.5 3.5 0 0 1 3.5 3.5C8.5 6 5 10 5 10S1.5 6 1.5 3.5A3.5 3.5 0 0 1 5 0zm0 2a1.5 1.5 0 1 0 0 3 1.5 1.5 0 0 0 0-3z"/></svg></span>Lindenweg 14b in 9412<br>Rudolfen</li>
    </ul>
  </section>

</main>
</body>
</html>
```